Trading company needs a non alcoholic beer Can design

We KLM are trading company , food Distributors in Africa -RD Congo/Kinshasa .We want to do a Private label non alcoholic beer 500ml can and need a design for this Project .
the Brand Name is : NUVA BREW
We want it to be similar NOT a copy of Velmora 0.0% can ( picture
attached ) as we want to respect the intellectual properties .so we prefer to use the same colors but more elegant ,modern style .
thanks.
THE DESIGN MUST STATE ITS A NON ALCOHOLIC BEER
PLZ SEARCH FOR VELMORA 0.0% MALT DRINK YOU WILL FIND 2 DESIGNS OLD AND NEW WE NEED SOMTHING SIMILAR TO THESE DESIGNS ,KINDLY USE SAME COLORS AND THE 0.0% SHOULD BE IN THE MIDDLE OF THE CAN .
Target Market(s)
THE PRODUCT WILL BE SOLD IN THE SUPERMASRKTS / MODERN TRADE

```html
<!DOCTYPE html>
<html lang="en">
<head>
<meta charset="utf-8">
<title>NUVA BREW 0.0% — Can Label</title>
<link rel="stylesheet" href="https://fonts.googleapis.com/css2?family=Anton&family=Cinzel:wght@600;700&family=Oswald:wght@500;600&family=Russo+One&display=swap">
<style>
  :root {
    --page: #ffffff;
    --red-light: #ff3a6e;
    --red-deep: #d0101e;
    --cream: #f6f2e6;
    --cream-shade: #e9e6da;
    --maroon: #7a1010;
    --ribbon-fold: #5a0808;
    --gold-cream: #f0dcb4;
    --royal-blue: #2350ff;
    --stripe: #d9d4c4;
    --ink: #111111;
    --white: #ffffff;
  }
  html, body {
    margin: 0;
    width: 1200px;
    height: 1185px;
    overflow: hidden;
    background: var(--page);
  }
  .label {
    position: absolute;
    left: 316px;
    top: 46px;
    width: 567px;
    height: 1092px;
  }
  .pattern-band { fill: url(#redSweep); }
  .pattern-tint { fill: var(--white); opacity: 0.08; }
  .base-band { fill: url(#redSweep); }
  .hairline { stroke: var(--white); stroke-width: 3; }
  .panel { fill: url(#creamSweep); }
  .panel-frame { fill: none; stroke: var(--maroon); stroke-width: 2.5; }
  .crest { fill: var(--maroon); }
  .ribbon { fill: var(--maroon); }
  .ribbon-fold { fill: var(--ribbon-fold); }
  .ribbon-word {
    font-family: "Cinzel", serif;
    font-weight: 700;
    font-size: 27px;
    fill: var(--gold-cream);
    letter-spacing: 1px;
  }
  .brand-band { fill: var(--royal-blue); }
  .brand-stripe { stroke: var(--stripe); stroke-width: 5; }
  .brand-name {
    font-family: "Russo One", sans-serif;
    font-size: 80px;
    fill: var(--white);
  }
  .abv {
    font-family: "Anton", sans-serif;
    font-size: 124px;
    fill: var(--ink);
  }
  .abv-unit {
    font-family: "Oswald", sans-serif;
    font-weight: 600;
    font-size: 40px;
    fill: var(--ink);
  }
  .product-type {
    font-family: "Oswald", sans-serif;
    font-weight: 500;
    font-size: 19px;
    letter-spacing: 3px;
    fill: var(--maroon);
  }
  .quality-small {
    font-family: "Cinzel", serif;
    font-weight: 600;
    font-size: 27px;
    fill: var(--gold-cream);
  }
  .quality-large {
    font-family: "Cinzel", serif;
    font-weight: 700;
    font-size: 44px;
    fill: var(--gold-cream);
  }
  .flourish { fill: var(--gold-cream); opacity: 0.85; }
</style>
</head>
<body>
<svg class="label" viewBox="993 465 540 1040" xmlns="http://www.w3.org/2000/svg" aria-label="NUVA BREW non-alcoholic beer can label">
  <defs>
    <linearGradient id="redSweep" x1="0" y1="0" x2="1" y2="0">
      <stop offset="0" stop-color="var(--red-light)"/>
      <stop offset="1" stop-color="var(--red-deep)"/>
    </linearGradient>
    <linearGradient id="creamSweep" x1="0" y1="0" x2="1" y2="0">
      <stop offset="0" stop-color="var(--cream)"/>
      <stop offset="1" stop-color="var(--cream-shade)"/>
    </linearGradient>
  </defs>

  <!-- top band -->
  <g class="top-band" role="img" aria-label="Red band with a leaf and swirl pattern">
    <path class="pattern-band" d="M993,580 C1060,580 1080,500 1150,485 Q1265,462 1380,485 C1450,500 1470,580 1533,580 L1533,740 L993,740 Z"/>
    <path class="pattern-tint" d="M993,580 C1060,580 1080,500 1150,485 Q1265,462 1380,485 C1450,500 1470,580 1533,580 L1533,740 L993,740 Z"/>
  </g>
  <line class="hairline" x1="993" y1="597" x2="1533" y2="597"/>

  <!-- base band -->
  <path class="base-band" d="M993,1250 L1533,1250 L1533,1390 C1470,1390 1450,1420 1420,1440 Q1265,1525 1110,1440 C1080,1420 1060,1390 993,1390 Z"/>

  <!-- cream panel -->
  <path class="panel" d="M993,725 L1040,725 L1040,685 L1130,685 C1170,650 1220,638 1265,638 C1310,638 1360,650 1400,685 L1490,685 L1490,725 L1533,725 L1533,1265 L1490,1265 L1490,1305 L1400,1305 C1360,1340 1310,1352 1265,1352 C1220,1352 1170,1340 1130,1305 L1040,1305 L1040,1265 L993,1265 Z"/>
  <path class="panel-frame" d="M1015,745 Q1050,745 1057,703 L1140,703 C1180,670 1220,657 1265,657 C1310,657 1350,670 1390,703 L1467,703 Q1475,745 1515,745 L1515,1245 Q1475,1245 1467,1285 L1390,1285 C1350,1320 1310,1333 1265,1333 C1220,1333 1180,1320 1140,1285 L1057,1285 Q1050,1245 1015,1245 Z"/>

  <!-- crest -->
  <rect class="crest" x="1200" y="672" width="135" height="78" rx="10" role="img" aria-label="Crown emblem"/>

  <!-- premium ribbon -->
  <g class="premium-ribbon">
    <polygon class="ribbon-fold" points="1158,790 1178,790 1178,820 1165,820 1172,806"/>
    <polygon class="ribbon-fold" points="1377,790 1357,790 1357,820 1370,820 1363,806"/>
    <path class="ribbon" d="M1170,775 Q1268,758 1365,775 L1365,808 Q1268,792 1170,808 Z"/>
    <text class="ribbon-word" x="1267" y="798" text-anchor="middle">PREMIUM</text>
  </g>

  <!-- brand band -->
  <polygon class="brand-band" points="1020,945 1517,810 1517,998 1020,1133"/>
  <line class="brand-stripe" x1="1020" y1="936" x2="1517" y2="800"/>
  <line class="brand-stripe" x1="1020" y1="1142" x2="1517" y2="1007"/>
  <text class="brand-name" x="1270" y="998" text-anchor="middle" textLength="450" lengthAdjust="spacingAndGlyphs" transform="rotate(-15.2 1270 970)">NUVA BREW</text>

  <!-- alcohol content -->
  <text class="abv" x="1270" y="1228" text-anchor="middle" textLength="280" lengthAdjust="spacingAndGlyphs">0.0%</text>
  <text class="abv-unit" x="1268" y="1282" text-anchor="middle">alc./vol.</text>
  <text class="product-type" x="1268" y="1312" text-anchor="middle">NON-ALCOHOLIC BEER</text>

  <!-- quality seal -->
  <text class="quality-small" x="1268" y="1383" text-anchor="middle">PREMIUM</text>
  <text class="quality-large" x="1268" y="1424" text-anchor="middle">QUALITY</text>
  <line class="hairline" x1="1112" y1="1437" x2="1415" y2="1437"/>
  <rect class="flourish" x="1192" y="1452" width="152" height="22" rx="11" role="img" aria-label="Decorative flourish"/>
</svg>
</body>
</html>
```